GRAPHICS FOR AN ICO WHITE PAPER DOCUMENT

For a new ICO launch of a Token on Blockchain, we need a new graphical setup of the White Paper document.
Consider that we want high impact in order to introduce the financial project, with several schemes, tables and graphs.
The actual logos are different and are provided attached.
Please send the first page as an example, an internal page, a sample of the argument list (in the final version they must be cliikable for fast moving inside the document), put the logo even small in every page and home button to get back to beginning. COMMENTS AND SUGGESTIONS ARE WELCOME WE WILL NEED CONTINUOUS COOPERATION WITH THE WINNER.

Target Market(s)

Investment, finance, blockchain

Industry/Entity Type

Investment Advisory

Font styles to use
Serif
Sans Serif
Decorative

Colors

Designer to choose colors to be used in the design.

Requirements
Must have
• End version in PDF small size, character size 15, distintive modern, neat look but dinamic, with right and left pages with different design, show movement of text between pages.
• Graphs, tables, easy to read and nice to see.
Nice to have
• EASY TO READ AND NAVIGATE
Should not have
• NO BORING STUFF!!!

```html
<!DOCTYPE html>
<html lang="en">
<head>
<meta charset="utf-8">
<title>NVX NovaTradeCapital Ltd. – Security Token Offering Whitepaper</title>
<link href="https://fonts.googleapis.com/css2?family=Fira+Sans:wght@400;600;700&display=swap" rel="stylesheet">
<style>
  :root {
    --ink: #1c1c1c;
    --paper: #ffffff;
    --brand-blue: #2d63b8;
    --band-top: #d9d9d9;
    --photo-light: #e7e9ea;
    --photo-mid: #9aa3a9;
    --photo-dark: #1e2a36;
    --photo-deep: #0d1116;
  }
  * { margin: 0; padding: 0; box-sizing: border-box; }
  html, body { width: 849px; height: 1200px; overflow: hidden; background: var(--paper); }
  .cover {
    position: relative;
    width: 849px;
    height: 1200px;
    overflow: hidden;
    font-family: "Fira Sans", sans-serif;
    color: var(--ink);
    background: var(--paper);
  }
  .running-head {
    position: absolute;
    top: 0; left: 0; right: 0;
    height: 52px;
    background: linear-gradient(to bottom, var(--band-top), var(--paper));
    font-size: 12.5px;
  }
  .running-head span { position: absolute; top: 24px; }
  .running-head .doc-title { left: 51px; }
  .running-head .doc-date { left: 362px; }
  .running-head .doc-site { left: 521px; }
  .running-head .doc-author { left: 679px; }

  .brand {
    position: absolute;
    top: 82px; left: 53px;
    display: flex; align-items: center; gap: 12px;
    color: var(--brand-blue);
  }
  .brand-dot {
    width: 80px; height: 80px; border-radius: 50%;
    background: var(--brand-blue);
  }
  .brand-name { font-size: 62px; font-weight: 700; letter-spacing: 1px; line-height: 1; }

  .company-name {
    position: absolute; top: 208px; left: 51px;
    font-size: 51px; font-weight: 700; letter-spacing: -0.3px;
  }
  .tagline {
    position: absolute; top: 284px; left: 52px;
    font-size: 43px; font-weight: 400;
  }
  .classification {
    position: absolute; top: 358px; left: 52px;
    font-size: 29px;
  }
  .offering-title {
    position: absolute; top: 418px; left: 51px;
    font-size: 29px; font-weight: 600;
  }
  .offering-date {
    position: absolute; top: 454px; left: 51px;
    font-size: 29px;
  }
  .hero-visual {
    position: absolute; top: 542px; left: 0;
    width: 849px; height: 658px;
    background:
      linear-gradient(160deg, transparent 48%, var(--photo-deep) 48.5%),
      linear-gradient(to bottom, var(--photo-dark) 0%, var(--photo-light) 12%, var(--photo-mid) 45%, var(--photo-dark) 100%);
  }
</style>
</head>
<body>
<main class="cover">
  <header class="running-head">
    <span class="doc-title">Security Token Offering Whitepaper</span>
    <span class="doc-date">August 2018</span>
    <span class="doc-site">www.nvtc.io</span>
    <span class="doc-author">Elena Ravelli</span>
  </header>

  <div class="brand">
    <div class="brand-dot"></div>
    <div class="brand-name">NVX</div>
  </div>

  <h1 class="company-name">NVX NovaTradeCapital Ltd.</h1>
  <p class="tagline">Your money growth</p>
  <p class="classification">Confidential</p>
  <h2 class="offering-title">Security Token Offering Whitepaper</h2>
  <p class="offering-date">Prepared August 2018</p>

  <div class="hero-visual" role="img" aria-label="Photo of a monitor showing trading charts in a softly lit office, black and white with blue tint"></div>
</main>
</body>
</html>
```